Sanora-Velantis Flyer Patient Day

We need a flyer for an event (format A5, double-sided, portrait format). This event is aimed at lymphology patients. The aim of this case is to inform patients about the progress of treatment, to show trends and to get in touch with them. The structure of the Flyer must be follows: - Page 1: with the title and date and logo of Sanora-Velantis - Page 2: with info text and details of the event The text templates are attached below: (180216_VA_Briefing_Workshopflyer_Betroffenentag_Sanora-Velantis.docx) The logos for the partners are also attached below. The following design inputs: 1) Please visit the following website: www.sanora-velantis.ch and use the logo of Sanora-Velantis 2) The visual language should be appropriate for the theme of networking (No Go people, preferably using graphical elements. ) Please use elements of the lymphology pathways, 3) For texts please use the following font: Roboto-Light For running text please use the following font: PT-Serif-Italic, sans-serif 4) The texts must be reader-friendly Please note that this flyer is not for Brevido, but for Sanora-Velantis.

```html
<!DOCTYPE html>
<html lang="de">
<head>
<meta charset="utf-8">
<title>Sanora-Velantis – Betroffenen- und Angehörigentag</title>
<link href="https://fonts.googleapis.com/css2?family=Roboto:wght@300;400;500&family=PT+Serif:ital,wght@1,400;1,700&display=swap" rel="stylesheet">
<style>
  :root {
    --green: #1fb38a;
    --teal: #18b38f;
    --teal-dark: #139a80;
    --label: #11706e;
    --leaf-dark: #2f7f2e;
    --leaf-light: #7cc045;
    --ink: #333;
    --partner-ink: #2a2f45;
    --white: #fff;
    --bg: #ecebe8;
  }
  * { margin: 0; padding: 0; box-sizing: border-box; }
  html, body { width: 1200px; height: 920px; overflow: hidden; background: var(--bg); }
  .canvas { position: relative; width: 1200px; height: 920px; }
  .page {
    position: absolute; top: 91px; width: 504px; height: 711px;
    background: var(--white); overflow: hidden;
    box-shadow: 0 4px 14px rgba(0,0,0,.18);
  }
  .page--front { left: 75px; }
  .page--back { left: 622px; }
  .abs { position: absolute; }
  .serif { font-family: 'PT Serif', serif; font-style: italic; }

  /* front */
  .brand { left: 34px; top: 52px; width: 120px; display: flex; flex-direction: column; align-items: center; gap: 10px;
    font-family: 'Roboto', sans-serif; font-weight: 400; font-size: 15px; color: var(--ink); }
  .brand__mark { width: 44px; height: 44px; background: var(--green); }
  .title { left: 179px; top: 36px; width: 310px; font-family: 'Roboto', sans-serif;
    font-weight: 300; font-size: 29px; line-height: 33px; color: var(--green); }
  .date { left: 179px; top: 141px; font-size: 18px; color: var(--ink); }
  .visual { left: 0; top: 197px; width: 504px; height: 397px;
    background: linear-gradient(100deg, var(--leaf-dark) 0%, var(--leaf-light) 28%, #3f9b3a 48%, var(--teal) 62%, var(--teal) 100%); }
  .coop { left: 23px; top: 629px; font-size: 15px; color: var(--ink); }
  .partner-name { display: flex; align-items: center; gap: 7px; font-family: 'Roboto', sans-serif;
    font-weight: 300; font-size: 11px; line-height: 13px; color: var(--ink); }
  .partner-name__dot { width: 10px; height: 10px; border-radius: 50%; background: var(--green); flex: none; }
  .strip { left: 0; top: 681px; width: 504px; height: 30px; }
  .strip--front { background: linear-gradient(90deg, var(--leaf-dark), var(--teal)); }
  .strip--back { background: var(--teal); }

  /* back */
  .intro { left: 78px; top: 28px; width: 360px; font-family: 'Roboto', sans-serif;
    font-weight: 300; font-size: 15.5px; line-height: 19px; color: var(--green); }
  .panel { left: 0; top: 130px; width: 504px; height: 467px; background: var(--teal);
    clip-path: polygon(60px 0, 504px 0, 504px 467px, 0 467px, 0 60px); }
  .program-bg { left: 66px; top: 288px; width: 372px; height: 171px; background: rgba(0,80,80,.08); }
  .rule { height: 1px; background: rgba(255,255,255,.85); left: 66px; width: 358px; }
  .label { right: 350px; height: 19px; padding: 0 10px; background: var(--label); color: var(--white);
    font-family: 'Roboto', sans-serif; font-size: 13px; line-height: 19px; }
  .val { left: 172px; color: var(--white); font-size: 12.5px; line-height: 15px; }
  .val b { font-weight: 700; }
  .list { left: 170px; top: 290px; list-style: none; color: var(--white); font-size: 13px; line-height: 18px; }
  .list li::before { content: ""; display: inline-block; border-left: 6px solid var(--white);
    border-top: 4px solid transparent; border-bottom: 4px solid transparent; margin-right: 6px; }
  .list .main { font-weight: 700; }
  .list .sub { padding-left: 38px; font-size: 12.5px; }
  .register { left: 0; top: 535px; width: 504px; height: 62px; background: var(--teal-dark);
    color: var(--white); text-align: center; padding-top: 10px;
    font-family: 'Roboto', sans-serif; font-size: 12.5px; line-height: 19px; }
  .register .serif { font-size: 15px; }
  .partner-label { left: 42px; top: 623px; font-size: 15px; color: var(--ink); }
  .sponsor { top: 624px; font-family: 'Roboto', sans-serif; font-weight: 400; font-size: 16px;
    line-height: 20px; color: var(--partner-ink); white-space: nowrap; }
</style>
</head>
<body>
<div class="canvas">

  <section class="page page--front">
    <div class="abs brand"><span class="brand__mark"></span><span>Sanora-Velantis</span></div>
    <h1 class="abs title">Betroffenen- und Angehörigentag Lip- und Lymphödem</h1>
    <p class="abs date serif">16. Jun 2018</p>
    <div class="abs visual" role="img" aria-label="Grünes Blatt in Nahaufnahme mit feinen Adern, rechts ein weisses Netzwerk aus Punkten und Linien als Sinnbild der Lymphbahnen"></div>
    <p class="abs coop serif">In Kooperation mit</p>
    <div class="abs partner-name" style="left:165px; top:626px;">
      <span class="partner-name__dot"></span>
      <span>Vereinigung Lipaura Schweiz</span>
    </div>
    <div class="abs partner-name" style="left:370px; top:626px;">
      <span>Lymvera Vereinigung<br>Schweiz</span>
    </div>
    <div class="abs strip strip--front"></div>
  </section>

  <section class="page page--back">
    <p class="abs intro">Die Stiftung Sanora-Velantis organisiert mit den beiden Betroffenenorganisationen Vereinigung Lipaura Schweiz und Lymvera Vereinigung Schweiz die folgende Tagung:</p>

    <div class="abs panel"></div>
    <div class="abs program-bg"></div>

    <span class="abs label" style="top:154px;">Datum</span>
    <p class="abs val serif" style="top:153px; font-size:16px; line-height:18px;">16. Juni 2018</p>
    <div class="abs rule" style="top:176px;"></div>

    <span class="abs label" style="top:180px;">Zeit</span>
    <p class="abs val serif" style="top:179px;"><b>ab 9h00</b>&nbsp; Eintreffen der Besucher<br>(Industrieausstellung geöffnet)</p>
    <p class="abs val serif" style="top:214px;"><b>ab 10h00</b>&nbsp; Start des Tagungsprogramms</p>
    <div class="abs rule" style="top:231px;"></div>

    <span class="abs label" style="top:236px;">Ort</span>
    <p class="abs val serif" style="top:235px;"><b>TBD, Aarau</b></p>
    <div class="abs rule" style="top:258px;"></div>

    <span class="abs label" style="top:263px;">Zielgruppe</span>
    <p class="abs val serif" style="top:263px;"><b>Betroffene und Angehörige</b></p>
    <div class="abs rule" style="top:286px;"></div>

    <span class="abs label" style="top:293px;">Programme</span>
    <ul class="abs list serif">
      <li class="main">Industrieausstellung</li>
      <li class="main">Darstellung Lip- und Lymphödem</li>
      <li class="main">Vorstellung der Organisationen</li>
      <li class="sub">Stiftung Sanora-Velantis</li>
      <li class="sub">Vereinigung Lipaura Schweiz</li>
      <li class="sub">Lymvera Vereinigung Schweiz</li>
      <li class="main">Ausgewogene Ernährung</li>
      <li class="main">Mode für Betroffene</li>
      <li class="main">Sport als Bestandteil der Therapie</li>
    </ul>
    <div class="abs rule" style="top:457px; width:367px;"></div>

    <span class="abs label" style="top:467px;">Eintritt:</span>
    <p class="abs val serif" style="top:467px; line-height:16px;">Teilnahmegebühren inkl. Mittagessen CHF 50.-<br>pro Person,<br>jede weitere Person CHF 15.</p>

    <div class="abs register">
      Anmeldungen und Fragen via E-mail : <span class="serif">info@sanora-velantis.ch</span><br>
      Anmeldefrist : 20 Mai 2018
    </div>

    <p class="abs partner-label serif">Partner</p>
    <span class="abs sponsor" style="left:139px;">Brevido</span>
    <span class="abs sponsor" style="left:262px;">Nordhal Medical</span>
    <span class="abs sponsor" style="left:406px;">Kelvera</span>

    <div class="abs strip strip--back"></div>
  </section>

</div>
</body>
</html>
```